Website incl. html for real estate project

We need the design and implementation of a website for a real estate project. Condominiums are built, which are sold.
We upload the sales brochure. The website should be based on the design of the sales brochure.
There are three houses with 5 apartments each. It should be rendered like this. The structure of the menu should be roughly as follows. Most information about the content is either in the appendix as a picture or in the brochure (PDF)):
Home (page 4-5 from the brochure)
House A
house B
house c
overview
basement
Municipal elections (page 6-7 in the brochure pdf)
Contact
Please use Roboto Regular as font.
And one page should give an overview of all apartments with the prices, the living space, etc. as on the file overview2.jpg.
If you go to the House A, House B, or House C menus, a page should come up with the details for that house only. The pages in the brochure are:
House A (Page 10-11)
House B (page 22-23)
House C (page 34-35)
The individual apartments should each be shown on a property page. There the plan / floor plan of the apartment and the pictures from the inside should be shown. As with the object page.jpg attachment.
Für die Designer... Mehr Zeit...
Coded - Design and coding required
1 page

```html
<!DOCTYPE html>
<html lang="de">
<head>
<meta charset="utf-8">
<title>Wohnpark am Erlenhain – Brunnhof Immobilien AG</title>
<link href="https://fonts.googleapis.com/css2?family=Roboto:wght@400;500;700&family=Old+Standard+TT:wght@400;700&display=swap" rel="stylesheet">
<style>
:root{
  --blue:#0a82d0;
  --red:#e0232e;
  --ink:#222;
  --text:#555;
  --muted:#888;
  --line:#dcdcdc;
  --grey:#f4f4f4;
  --dark:#1d2733;
  --white:#fff;
  --foot-text:#e6e9ec;
}
*{margin:0;padding:0;box-sizing:border-box}
html,body{width:1200px;height:4789px;overflow:hidden}
body{position:relative;background:var(--white);font-family:'Roboto',sans-serif;color:var(--text);font-size:10.5px;line-height:15px}
.abs{position:absolute}
.serif{font-family:'Old Standard TT',serif;color:var(--ink);font-weight:400}

/* header */
.site-header{left:0;top:0;width:1200px;height:74px;background:var(--white)}
.brand{left:74px;top:18px;display:flex;align-items:center;gap:8px}
.brand-name{font-family:'Roboto',sans-serif;font-weight:700;font-size:19px;letter-spacing:.5px;color:var(--blue);line-height:20px}
.brand-sub{font-size:8px;letter-spacing:2px;color:var(--blue);font-weight:700;line-height:10px}
.brand-mark{width:12px;height:12px;background:var(--red)}
.main-nav{left:298px;top:31px;display:flex;gap:24px;font-size:9px;text-transform:uppercase;color:#444;letter-spacing:.3px}
.main-nav .active{color:var(--blue)}
.header-contact{right:74px;top:22px;text-align:right;font-family:'Old Standard TT',serif;font-size:11px;color:#444;line-height:18px}
.header-contact .mail{color:var(--red)}

/* hero */
.hero-accent{left:407px;top:420px;width:793px;height:123px;background:var(--blue)}
.hero-photo{left:0;top:74px;width:1125px;height:406px;background:linear-gradient(180deg,#dfe7ee 0%,#cfd6d8 45%,#8c9a7c 75%,#5f7a3f 100%)}
.hero-marker{width:14px;height:14px;border:2px solid #222;border-radius:50%;background:#fff}
.hero-marker::after{content:"";position:absolute;left:3px;top:3px;width:4px;height:4px;border-radius:50%;background:#222}
.hero-tag{left:703px;top:174px;font-size:20px;line-height:24px}
.hero-stem{left:695px;top:172px;width:2px;height:70px;background:#222}

/* intro */
.title-xl{font-size:44px;line-height:50px}
.rule{height:3px;width:61px;background:var(--blue)}
.copy p{margin-bottom:12px}

/* stats */
.stats-band{left:0;top:1260px;width:1200px;height:125px;background:var(--grey)}
.stat{top:1173px;width:201px;height:149px;background:var(--white);border:1.5px solid var(--blue);border-radius:3px;text-align:center}
.stat-num{font-family:'Old Standard TT',serif;font-size:44px;line-height:50px;color:var(--blue);margin-top:26px}
.stat-label{font-size:10.5px;line-height:14px;color:#555;margin-top:8px}

/* plan */
.plan-frame{left:200px;top:1550px;width:800px;height:380px;border-right:5px solid var(--blue);border-bottom:5px solid var(--blue)}
.plan-img{left:200px;top:1550px;width:795px;height:375px;background:linear-gradient(135deg,#efefef,#dedede 50%,#e8ebe0)}

/* houses */
.houses-band{left:0;top:2002px;width:1200px;height:229px;background:var(--grey)}
.photo{background:linear-gradient(180deg,#e4e8ec 0%,#c9cfd1 50%,#7f9567 80%,#4f6e33 100%)}
.house-panel{background:var(--white);padding:20px 0 0 26px}
.house-panel h3,.house-side h3{font-family:'Old Standard TT',serif;font-size:28px;font-weight:400;color:var(--ink);line-height:32px;margin-bottom:14px}
.unit-table{border-collapse:collapse;font-size:10px;color:#555}
.unit-table td{height:31px;border-bottom:1px solid var(--line);padding:0;vertical-align:middle;white-space:nowrap}

/* contact */
.contact-band{left:0;top:3779px;width:1200px;height:539px;background:var(--grey)}
.map{left:201px;top:3910px;width:304px;height:304px;border-radius:50%;background:radial-gradient(circle at 45% 45%,#f3f2ee,#e3e6df 70%,#d7dbd2)}
.field{background:var(--white);border:1px solid #e2e2e2;font-size:9px;color:#777;padding:8px 12px}
.btn{background:var(--red);color:var(--white);font-family:'Old Standard TT',serif;font-weight:700;font-size:11px;display:flex;align-items:center;justify-content:center}

/* footer */
.footer{left:0;top:4318px;width:1200px;height:471px;background:var(--dark)}
.footer-accent{left:0;top:4318px;width:587px;height:64px;background:var(--blue)}
.footer-title{font-family:'Old Standard TT',serif;font-weight:700;font-size:17px;line-height:20px;color:var(--white)}
.foot-txt{color:var(--foot-text);font-size:10px}
.sitemap{list-style:none;font-size:9px;text-transform:uppercase;color:var(--foot-text);line-height:22.7px;font-weight:500}
.social{width:30px;height:30px;border-radius:50%;background:#3b4652}
.social.on{background:var(--blue)}
.footer-rule{left:200px;top:4722px;width:800px;height:1px;background:#34404c}
</style>
</head>
<body>

<header class="site-header abs">
  <div class="brand abs">
    <span class="brand-mark"></span>
    <div><div class="brand-name">BRUNNHOF</div><div class="brand-sub">IMMOBILIEN AG</div></div>
  </div>
  <nav class="main-nav abs">
    <span class="active">Startseite</span><span>Haus A</span><span>Haus B</span><span>Haus C</span><span>Untergeschoss</span><span>Gemeinde Talbach</span><span>Kontakt</span>
  </nav>
  <div class="header-contact abs">
    <div>&#9742; +41 61 555 20 40</div>
    <div class="mail">&#9993; info@brunnhof-immo.ch</div>
  </div>
</header>

<div class="hero-accent abs"></div>
<div class="hero-photo abs" role="img" aria-label="Visualisierung der drei Mehrfamilienhäuser mit Garten und Bäumen"></div>
<div class="hero-marker abs" style="left:399px;top:191px"></div>
<div class="hero-stem abs"></div>
<div class="hero-marker abs" style="left:689px;top:240px"></div>
<div class="hero-tag abs serif">Haus B</div>

<h1 class="abs serif title-xl" style="left:200px;top:598px">Wohnpark am Erlenhain</h1>
<div class="abs rule" style="left:200px;top:665px"></div>

<div class="abs copy" style="left:407px;top:697px;width:592px">
  <p>Die Überbauung mit drei Mehrfamilienhäusern und insgesamt 15 Eigentumswohnungen entsteht zwischen der Bachstrasse und dem Rainweg in Talbach bei Birsau.</p>
  <p>Die modernen und hochwertigen Wohnungen sind gegen das ruhige Quartier Rainmatt und den wunderschönen Ausblick auf die grüne «Hochwacht» ausgerichtet.</p>
  <p>Die Wohnungen befinden sich an idealer Lage in Talbach mit guter Besonnung und die nächste Bushaltestelle ist nur knapp 120 Meter entfernt. Die Wohnungen im Obergeschoss mit grosszügigem Balkon und im Erdgeschoss mit einem gedeckten Sitzplatz und eigenem Garten ausgestattet.</p>
  <p>Der Wohnpark verfügt über ein grosszügiges, gemeinsames Parkhaus, von dem aus in jedes Gebäude ein Lift auf die gewünschte Etage führt. Jede Wohnung verfügt über einen eigenen Keller / ein eigenes Kellerabteil. Zudem ist im Keller ein Schutzraum für die Bewohner vorhanden.</p>
</div>
<div class="abs copy" style="left:200px;top:914px;width:592px">
  <p>Das Gebäude wird mit 18 bis 30 cm atmungsaktiver Steinwolle isoliert. Geheizt wird über eine moderne Wärmepumpe im Verbund mit einer Photovoltaikanlage, ökologisch hocheffizient mit zeitgemässer Technologie, unabhängig von steigenden Gas und Ölpreisen.</p>
  <p>Alle Wohnungen besitzen einen grosszügigen Wohn-, Koch-/ Essbereich mit raumhohen Fenstern verglast, was für eine helle und freundliche Atmosphäre sorgt.</p>
  <p>Die Umgebungsgestaltung passt perfekt in die ruhige, natürliche und trotzdem moderne Umgebung. Die grosszügigen Grünflächen der Erdgeschosswohnungen und die dezente Grundbepflanzung verbunden mit den Wegen runden die moderne und zeitlose Architektur des Gebäudes ab.</p>
  <p>Die Wohnungen werden schlüsselfertig zum Fixpreis abgegeben. Es besteht darüber hinaus die Möglichkeit den Innenausbau nach eigenen Wünschen in verschiedenen Bereichen massgeblich mitzugestalten.</p>
</div>

<div class="stats-band abs"></div>
<div class="stat abs" style="left:74px"><div class="stat-num">3</div><div class="stat-label">Gebäude mit individuellem<br>Wohnangebot</div></div>
<div class="stat abs" style="left:287px"><div class="stat-num">9</div><div class="stat-label">unterschiedliche<br>Grundrisstypen</div></div>
<div class="stat abs" style="left:500px"><div class="stat-num">27</div><div class="stat-label">Parkplätze in der<br>Tiefgarage</div></div>
<div class="stat abs" style="left:713px"><div class="stat-num">15</div><div class="stat-label">komfortable<br>Wohnungen</div></div>
<div class="stat abs" style="left:926px"><div class="stat-num">120</div><div class="stat-label">Meter bis zur<br>Bushaltestelle</div></div>

<h2 class="abs serif title-xl" style="left:0;top:1449px;width:1200px;text-align:center">Übersichtsplan</h2>
<div class="abs rule" style="left:570px;top:1517px"></div>
<div class="plan-frame abs"></div>
<div class="plan-img abs" role="img" aria-label="Situationsplan mit Haus A, Haus B und Haus C zwischen zwei Quartierstrassen"></div>

<div class="houses-band abs"></div>
<h2 class="abs serif title-xl" style="left:0;top:2044px;width:1200px;text-align:center">Die Häuser</h2>
<div class="abs rule" style="left:570px;top:2112px"></div>

<!-- Haus A -->
<div class="abs photo" style="left:200px;top:2147px;width:594px;height:312px" role="img" aria-label="Visualisierung Haus A mit Garten und Sitzplätzen"></div>
<div class="abs house-panel" style="left:587px;top:2231px;width:413px;height:167px">
  <h3>Haus A</h3>
  <p>Das Gebäude «Haus A» verfügt über fünf moderne Wohnungen mit individuellen Grundrissen. Alle Wohnungen haben einen grosszügigen Aussenbereich mit Balkon oder gedecktem Sitzplatz in Richtung Süden zur Hochwacht, dem Talbacher Hausberg. Die Wohnräume sind mit grossen Fenstern ausgestattet, was die Räume mit Sonnenlicht durchflutet. Das Gebäude ist direkt aus der Tiefgarage mit dem Lift zugänglich.</p>
</div>
<table class="abs unit-table" style="left:200px;top:2460px;width:594px">
  <colgroup><col style="width:118px"><col style="width:89px"><col style="width:138px"><col></colgroup>
  <tr><td>Attika Wohnung</td><td>4.5 Zimmer</td><td>108 m2 Wohnfläche</td><td>105 m2 grosse Sonnenterrasse !</td></tr>
  <tr><td>Obergeschoss</td><td>3.5 Zimmer</td><td>81 m2 Wohnfläche</td><td>16 m2 grosser Balkon</td></tr>
  <tr><td>Obergeschoss</td><td>4.5 Zimmer</td><td>102 m2 Wohnfläche</td><td>33 m2 grosser Balkon</td></tr>
  <tr><td>Erdgeschoss</td><td>3.5 Zimmer</td><td>81 m2 Wohnfläche</td><td>16 m2 gedeckter Sitzplatz und über 120 m² Garten</td></tr>
  <tr><td>Erdgeschoss</td><td>4.5 Zimmer</td><td>102 m2 Wohnfläche</td><td>33 m2 gedeckter Sitzplatz und über 120 m² Garten</td></tr>
</table>

<!-- Haus B -->
<div class="abs photo" style="left:407px;top:2666px;width:593px;height:312px" role="img" aria-label="Visualisierung Haus B mit Terrassen und Sonnenschirmen"></div>
<div class="abs house-side" style="left:200px;top:2765px;width:376px">
  <h3>Haus B</h3>
  <p>Das Gebäude «Haus B» verfügt über fünf moderne Wohnungen mit individuellen Grundrissen. Alle Wohnungen haben einen grosszügigen Balkon oder Terrasse Richtung Süden zur Hochwacht, dem Talbacher Hausberg, ausgerichtet. Die Wohnräume sind mit grossen Fenstern ausgestattet, was die Räume mit hellem Sonnenlicht durchflutet. Das Gebäude ist direkt aus der Tiefgarage mit dem Lift zugänglich.</p>
</div>
<table class="abs unit-table" style="left:407px;top:2979px;width:593px">
  <colgroup><col style="width:117px"><col style="width:89px"><col style="width:138px"><col></colgroup>
  <tr><td>Attika Wohnung</td><td>4.5 Zimmer</td><td>109 m2 Wohnfläche</td><td>107 m2 grosse Sonnenterrasse !</td></tr>
  <tr><td>Obergeschoss</td><td>2.5 Zimmer</td><td>69 m2 Wohnfläche</td><td>14 m2 grosse Balkon</td></tr>
  <tr><td>Obergeschoss</td><td>4.5 Zimmer</td><td>117 m2 Wohnfläche</td><td>42 m2 grosse Balkon</td></tr>
  <tr><td>Erdgeschoss</td><td>2.5 Zimmer</td><td>69 m2 Wohnfläche</td><td>14 m2 gedeckter Sitzplatz und über 70 m² Garten</td></tr>
  <tr><td>Erdgeschoss</td><td>4.5 Zimmer</td><td>117 m2 Wohnfläche</td><td>42 m2 gedeckter Sitzplatz und über 140 m² Garten</td></tr>
  <tr><td>Untergeschoss</td><td>Hobbyraum</td><td>24 m2 Flächen</td><td></td></tr>
</table>

<!-- Haus C -->
<div class="abs photo" style="left:200px;top:3220px;width:594px;height:310px" role="img" aria-label="Visualisierung Haus C mit Garten"></div>
<div class="abs house-panel" style="left:587px;top:3301px;width:413px;height:167px">
  <h3>Haus C</h3>
  <p>Das Gebäude «Haus C» verfügt über fünf moderne Wohnungen mit individuellen und gross angelegten Grundrissen. Alle Wohnungen haben einen grosszügigen Balkon oder Terrasse in Richtung Hochwacht, dem Talbacher Hausberg. Die Wohnräume sind mit grossen Fenstern ausgestattet, was die Räume mit Sonnenlicht durchflutet. Das Gebäude ist direkt aus der Tiefgarage mit dem Lift zugänglich.</p>
</div>
<table class="abs unit-table" style="left:200px;top:3531px;width:594px">
  <colgroup><col style="width:118px"><col style="width:89px"><col style="width:138px"><col></colgroup>
  <tr><td>Attika Wohnung</td><td>4.5 Zimmer</td><td>129 m2 Wohnfläche</td><td>132 m2 grosse Sonnenterrasse !</td></tr>
  <tr><td>Obergeschoss</td><td>5.5 Zimmer</td><td>143 m2 Wohnfläche</td><td>43 m2 grosser Balkon</td></tr>
  <tr><td>Obergeschoss</td><td>3.5 Zimmer</td><td>96 m2 Wohnfläche</td><td>23 m2 grosser Balkon</td></tr>
  <tr><td>Erdgeschoss</td><td>5.5 Zimmer</td><td>143 m2 Wohnfläche</td><td>43 m2 gedeckter Sitzplatz und über 120 m² Garten</td></tr>
  <tr><td>Erdgeschoss</td><td>3.5 Zimmer</td><td>96 m2 Wohnfläche</td><td>23 m2 gedeckter Sitzplatz und über 60 m² Garten</td></tr>
  <tr><td>Untergeschoss</td><td>Hobbyraum</td><td>43 m2 Fläche</td><td>mit Dusche/Lavabo und Toilette</td></tr>
</table>

<!-- Kontakt -->
<div class="contact-band abs"></div>
<h2 class="abs serif title-xl" style="left:0;top:3836px;width:1200px;text-align:center">Kontakt</h2>
<div class="abs rule" style="left:570px;top:3889px"></div>
<div class="map abs" role="img" aria-label="Kartenausschnitt der Region mit Standortmarkierung des Wohnparks"></div>
<div class="abs serif" style="left:613px;top:3955px;font-size:28px;line-height:32px">Schreiben Sie uns</div>
<p class="abs" style="left:613px;top:4003px;width:387px;font-size:9.5px">Wir freuen uns auf Ihre Anfrage zu den Wohnungen im Wohnpark. Unser Team meldet sich gerne zeitnah bei Ihnen zurück.</p>
<div class="abs field" style="left:613px;top:4054px;width:186px;height:30px">Name</div>
<div class="abs field" style="left:814px;top:4054px;width:186px;height:30px">Email</div>
<div class="abs field" style="left:613px;top:4097px;width:387px;height:76px">Message</div>
<div class="abs btn" style="left:613px;top:4188px;width:99px;height:32px">Get in Touch</div>

<!-- Footer -->
<div class="footer abs"></div>
<div class="footer-accent abs"></div>
<div class="abs" style="left:200px;top:4445px">
  <div class="brand-name" style="color:#fff;font-size:22px;line-height:24px">BRUNNHOF</div>
  <div class="brand-sub" style="color:#fff;margin-top:4px">IMMOBILIEN AG</div>
</div>
<div class="abs foot-txt" style="left:200px;top:4508px;line-height:23px">
  <div style="font-family:'Old Standard TT',serif;font-size:15px"><span style="color:var(--blue)">&#9742;</span> +41 61 555 20 40</div>
  <div><span style="color:var(--blue)">&#9993;</span> info@brunnhof-immo.ch</div>
  <div style="line-height:14px;margin-top:4px;display:flex;gap:8px">
    <svg width="10" height="14" viewBox="0 0 10 14"><path d="M5 0a5 5 0 0 1 5 5c0 4-5 9-5 9S0 9 0 5a5 5 0 0 1 5-5z" fill="#0a82d0"/><circle cx="5" cy="5" r="2" fill="#1d2733"/></svg>
    <span>Brunnhof Immobilien AG<br>Talstrasse 8, 4250 Talbach</span>
  </div>
</div>

<div class="abs footer-title" style="left:437px;top:4452px">Sitemap</div>
<ul class="sitemap abs" style="left:439px;top:4505px">
  <li>Startseite</li><li>Kontakt</li><li>Haus A</li><li>Haus B</li><li>Haus C</li><li>Untergeschoss</li><li>Gemeinde Talbach</li><li>Impressum</li>
</ul>

<div class="abs footer-title" style="left:613px;top:4452px">Newsletter</div>
<p class="abs foot-txt" style="left:613px;top:4512px;width:276px;font-size:9px;line-height:14px">Melden Sie sich an und erhalten Sie alle Neuigkeiten zum Baufortschritt und zu freien Wohnungen.</p>
<div class="abs field" style="left:613px;top:4575px;width:276px;height:30px;background:transparent;border-color:#6b7580;color:#e6e9ec">Enter Your Email ...</div>
<div class="abs btn" style="left:613px;top:4620px;width:99px;height:28px">Submit</div>

<div class="social abs" style="left:970px;top:4458px"></div>
<div class="social on abs" style="left:970px;top:4495px"></div>

<div class="footer-rule abs"></div>
<p class="abs" style="left:200px;top:4751px;font-size:9px;color:#cfd4d9">© 2022 <span style="color:var(--blue)">Brunnhof Immobilien AG</span>. All Rights Reserved</p>
<svg class="abs" style="left:1090px;top:4740px" width="20" height="22" viewBox="0 0 20 22"><path d="M2 21 10 2l8 19M5 14h10" fill="none" stroke="#0a82d0" stroke-width="1.5"/></svg>

</body>
</html>
```